Successful Health Company Needs a Face Lift

We need a beautiful new design for our existing, online health supplements business.

Most of the elements are already there, but we need your sophistication and style.

The 3 pages that need your magic touch are:
Home page:
http://www.vitalbloom.co.uk

Multiple Product pages. e.g:
http://www.vitalbloom.co.uk/health-issues/major-organs/skin-hair-nails.html

Single Product pages. e.g:
http://www.vitalbloom.co.uk/l-arginine-500-mg.html

Please have a look around.

This is a bilingual site, so all text (except logo) needs to be easily changed/translated. If photoshop files can be provided where we can simply translate the text layer of a graphic, that is acceptable. Please note that Greman words are generally longer than English.

Appearance:
The over all look should be open, light, uplifting and sophisticated.

The Home Page in detail:
We are largely happy with the category boxes in the centre column although you may restyle these if you wish.
The header, left menu and right column don't hang together and need your skills.

Logo:
We would like you to enhance our logo, but please note the 'S' and circle are used on many product labels, so we can't go too far from this just now.
(Product label example: http://www.vitalbloom.co.uk/black-walnut-tincture-from-green-hull.html)

Header:
This needs to imply health and be light and stylish without it taking up valuable room.

Left Menu:
This is a multi-layer concertina menu. It is hard to see where your are within it. It needs to be made more clear and easy to navigate, maybe by using indentation and or better colour choices.
Please show it expanded and condensed in your design proposals.
(Extended menu example: http://www.vitalbloom.co.uk/health-issues/female-health/thrush.html)

Multiple Product pages in detail
Please style the the brief descriptions, which must contain bullet points, price, add to basket and learn more.

Single Product pages in detail
The design and layout of this page needs to include all the elements currently there, including price, Qty, Add to Basket button, size and article number.

The static blocks on the right column will appear on these single product pages and need to suit the design well. They should not over-power the central content of the page.
Updates

Thank you all for participating.

Please note that what we are looking for is a more stylish and attractive version of what we already have.  The elements are all there.  We are not looking for a new concept.

We are happy for designers to switch images for better ones, work with colour ways, alter proportions and insert the elements in our brief.

We do not want to add banners, large images etc.  We want our customers to be familiar with what they see, and to be impressed with how much better the pages hang together.  They should not think they've landed at a new company.

We do want to see how the left menu looks when extended to show 2nd and 3rd tier menu titles.
We will also want to see how the design works for a multiple product page like this: http://www.vitalbloom.co.uk/supplement-type/anti-microbials.html
as well as a single product page like this:  http://www.vitalbloom.co.uk/black-walnut-extract.html

Some adjustment to the 'VitalBloom' logo is also an option and the graphic has been attached. 

Thank you for your careful attention to our brief.

Marcus.
pp Anselm

Project Deadline Extended
Reason: Due to unanticipated travel arrangements, the company director will only be available to make final decisions on Monday the 19th of March. Please continue updating submissions as we are in touch. Thank you for your understanding.

Target Market(s)

Health conscious women 70% men 30% aged 40 to 65 and health practitioners.

Industry/Entity Type

Health

Requirements
Must have
• Please include in the Header:
UK and German flags
Chatterbook, pok, +1, quiller, joined up, wander into
Padlock/SSL security/secure transaction
Practitioner helpline/ orders phone number
Fundwire/Credit card logo

Please include in right column:
Clinician Nook
Amalgam Clear Dental
Shopping Basket
Storefronts for Therapists

Please include in either Header or Right Column
Same day dispatch
Money back warranty

```html
<!DOCTYPE html>
<html lang="en">
<head>
<meta charset="utf-8">
<title>VitalBloom Enterprises – Home</title>
<link rel="stylesheet" href="https://fonts.googleapis.com/css2?family=Open+Sans:wght@400;600;700&family=PT+Sans:wght@400;700&display=swap">
<style>
:root{
  --teal:#2ab0d4;
  --teal-dark:#2b7f86;
  --aqua:#a9ecef;
  --aqua-strong:#82e0e5;
  --aqua-pale:#eefafa;
  --tab:#7db6dc;
  --tab-dark:#5a9ecd;
  --pink:#e8336f;
  --pink-soft:#fbd6e4;
  --grey-bg:#f3f3f3;
  --grey-line:#dcdcdc;
  --text:#333;
  --muted:#666;
  --gold:#e5b21c;
  --brown:#6b3a1a;
}
*{box-sizing:border-box;margin:0;padding:0}
html,body{width:1008px;height:1200px;overflow:hidden;background:#fff}
body{position:relative;font-family:"Open Sans",Arial,sans-serif;color:var(--text)}
.abs{position:absolute}
a{color:inherit;text-decoration:none}

/* top utility bar */
.utility{left:585px;top:0;width:386px;height:36px;background:linear-gradient(#fff,#ececec);border-bottom-left-radius:30px;border:1px solid #e2e2e2;border-top:0;border-right:0}
.flag{top:10px;width:22px;height:15px}
.account{left:108px;top:10px;font-size:11px;color:#222;white-space:nowrap}
.social{top:8px;width:19px;height:19px;border-radius:3px}
.count{left:352px;top:8px;width:22px;height:19px;border:1px solid #ccc;background:#fff;font-size:11px;text-align:center;line-height:17px;color:#555}

/* brand */
.brand-mark{left:30px;top:25px;width:66px;height:66px;border-radius:50%;border:5px solid #d98ab0;background:#fff}
.brand-name{left:112px;top:22px;font-family:"PT Sans",sans-serif;font-size:43px;letter-spacing:1px;color:#5bbfd6;font-weight:400;line-height:1.1;white-space:nowrap}
.brand-sub{left:268px;top:64px;font-family:"PT Sans",sans-serif;font-size:11px;letter-spacing:1.5px;color:#5bbfd6;white-space:nowrap}

/* cart */
.cart{left:773px;top:50px}
.cart-title{left:31px;top:0;font-size:15px;color:var(--pink);white-space:nowrap}
.cart-note{left:32px;top:22px;font-size:10.5px;color:var(--muted);white-space:nowrap}
.cart-link{left:32px;top:40px;font-size:10px;color:var(--pink);white-space:nowrap}

/* main nav */
.nav-tab{top:115px;height:38px;background:linear-gradient(var(--tab),var(--tab-dark));border-radius:12px 28px 0 0;color:#fff;font-family:"PT Sans",sans-serif;font-weight:700;font-size:15px;padding:9px 0 0 10px;letter-spacing:.3px;white-space:nowrap}
.search-tab{left:697px;top:115px;width:274px;height:38px;background:linear-gradient(#fbfbfb,#e9e9e9);border-radius:34px 0 0 0;border:1px solid #ddd;border-bottom:0}
.search-input{left:40px;top:9px;width:228px;height:22px;background:#fff;border:1px solid #ccc;border-radius:11px;font-size:12px;color:#555;padding:3px 9px}
.search-btn{left:248px;top:12px;width:17px;height:17px;border-radius:4px;background:var(--pink)}

/* assurance bar */
.assure{left:28px;top:153px;width:943px;height:72px;background:linear-gradient(#fafafa,#e6e6e6);border-bottom:1px solid #d6d6d6}
.divider{top:0;width:1px;height:72px;background:#d0d0d0}
.secure{left:62px;top:11px;font-family:"PT Sans",sans-serif;font-size:17px;color:#444;white-space:nowrap}
.secure b{color:#c8285e}
.pay-card{top:38px;width:30px;height:19px;border-radius:3px;border:1px solid #999}
.helpline{left:305px;top:8px;width:312px;text-align:center;font-family:"PT Sans",sans-serif;font-size:15px;color:#555;white-space:nowrap}
.phone{left:305px;top:26px;width:312px;text-align:center;font-family:"PT Sans",sans-serif;font-size:30px;color:var(--pink);letter-spacing:.5px;white-space:nowrap}
.promise{font-family:"PT Sans",sans-serif;color:#444;line-height:1;white-space:nowrap}
.promise .big{font-size:18px;display:block}
.promise .small{font-size:12.5px;display:block;margin-top:2px}

/* side menu */
.side-menu{left:28px;top:235px;width:183px}
.menu-item{position:relative;height:33px;margin-bottom:1.6px;background:var(--aqua);font-size:13.5px;color:var(--teal-dark);padding:7px 0 0 12px;white-space:nowrap}
.menu-item.is-top{background:var(--aqua-strong);padding-left:17px}
.menu-item .toggle{position:absolute;right:0;top:0;width:33px;height:33px;background:var(--aqua-strong);border-left:1px solid #c7f3f5}
.menu-item.is-top .toggle{background:transparent}
.toggle svg{position:absolute;left:9px;top:9px}

.newsletter{left:28px;top:686px;width:183px;height:125px;background:var(--aqua-pale);border:1px solid #cdeef0}
.nl-title{text-align:center;font-family:"PT Sans",sans-serif;color:#2b8f93;line-height:1;margin-top:10px;white-space:nowrap}
.nl-title span{display:block;font-size:20px}
.nl-title strong{display:block;font-size:25px;font-weight:400;margin-top:1px}
.nl-input{left:9px;top:58px;width:164px;height:24px;background:var(--aqua-strong);color:#fff;font-size:11px;padding:5px 7px}
.nl-btn{left:9px;top:88px;width:59px;height:24px;border-radius:8px;background:var(--aqua-strong);color:#fff;font-size:11px;font-weight:700;text-align:center;line-height:24px}

/* category grid */
.cat{width:269px;height:122px;border:1px solid #ddd;background:#fff;overflow:hidden}
.cat h3{position:absolute;left:10px;top:6px;font-size:14px;font-weight:400;color:var(--teal);text-decoration:underline;text-underline-offset:2px;font-family:Arial,sans-serif;white-space:nowrap}
.cat ul{position:absolute;left:10px;top:30px;list-style:none;font-size:10.5px;line-height:17.4px;color:#222;white-space:nowrap}
.cat li::before{content:"";display:inline-block;border-left:4px solid #555;border-top:3px solid transparent;border-bottom:3px solid transparent;margin-right:6px;vertical-align:1px}
.cat .pic{position:absolute;right:0;top:0;width:145px;height:120px}

/* right column */
.promo{left:789px;width:182px;overflow:hidden}
.hub{top:235px;height:154px;border:1px solid #9fd6e3;background:linear-gradient(#fff9e8,#ffe9c8);border-radius:8px}
.hub-head{height:33px;background:linear-gradient(#bff2f6,#70d6e3);font-family:"PT Sans",sans-serif;font-size:18px;color:#222;padding:4px 9px;white-space:nowrap}
.promo-copy{font-family:"PT Sans",sans-serif;color:var(--brown);line-height:1.05;white-space:nowrap}
.dental{top:400px;height:154px;border:1px solid #9fd6e3;background:#fff;border-radius:8px}
.basket{top:564px;height:122px;background:var(--pink-soft);border-radius:8px}
.basket-tag{left:0;top:0;width:118px;height:50px;background:#f04a86;border-radius:8px 0 40px 0;color:#fff;font-family:"PT Sans",sans-serif;font-size:17px;line-height:1.05;padding:7px 9px}
.stores{top:696px;height:162px;background:radial-gradient(circle at 50% 40%,#f0508d,#d3145a);border-radius:8px}
.stores-copy{left:0;top:116px;width:182px;text-align:center;color:#fff;font-family:"PT Sans",sans-serif;font-size:19px;line-height:1.05}

/* footer */
.footer{left:28px;top:966px;width:943px;height:145px;background:var(--grey-bg);border:1px solid var(--grey-line);border-radius:4px}
.foot-col{top:13px;list-style:none;font-size:10.5px;line-height:20.4px;color:#1f8fb4;white-space:nowrap}
.foot-col li::before{content:"";display:inline-block;border-left:3px solid #888;border-top:2.5px solid transparent;border-bottom:2.5px solid transparent;margin-right:5px;vertical-align:1px}
.foot-links{left:0;top:112px;width:943px;text-align:center;font-size:10.5px;color:#222;word-spacing:2px;white-space:nowrap}
.foot-links a{margin:0 6px}
.base-line{left:18px;top:1143px;width:962px;height:1px;background:#c9e5ea}
.base-mark{left:40px;top:1123px;width:42px;height:42px;border-radius:50%;border:4px solid #d98ab0;background:#fff}
.copyright{left:104px;top:1137px;font-size:10.5px;color:#222;background:#fff;padding-right:6px;white-space:nowrap}
</style>
</head>
<body>

<!-- utility bar -->
<div class="abs utility">
  <svg class="abs flag" style="left:39px" viewBox="0 0 22 15" aria-label="Deutsch"><rect width="22" height="5" fill="#111"/><rect y="5" width="22" height="5" fill="#d00"/><rect y="10" width="22" height="5" fill="#fc0"/></svg>
  <svg class="abs flag" style="left:71px" viewBox="0 0 22 15" aria-label="English"><rect width="22" height="15" fill="#012169"/><path d="M0 0L22 15M22 0L0 15" stroke="#fff" stroke-width="3"/><path d="M0 0L22 15M22 0L0 15" stroke="#c8102e" stroke-width="1"/><path d="M11 0V15M0 7.5H22" stroke="#fff" stroke-width="4"/><path d="M11 0V15M0 7.5H22" stroke="#c8102e" stroke-width="2"/></svg>
  <div class="abs account"><a href="#">Login</a> &nbsp;|&nbsp; <a href="#">Register</a></div>
  <span class="abs social" style="left:200px;background:#3fb6e6" aria-label="quiller"></span>
  <span class="abs social" style="left:223px;background:#3b5998" aria-label="Chatterbook"></span>
  <span class="abs social" style="left:246px;background:#2e9bd6" aria-label="wander into"></span>
  <span class="abs social" style="left:270px;background:#2a73b5" aria-label="joined up"></span>
  <span class="abs social" style="left:293px;background:#1f5f9e" aria-label="pok"></span>
  <span class="abs social" style="left:317px;width:31px;background:#e9eef3;border:1px solid #bbb" aria-label="+1"></span>
  <span class="abs count">2</span>
</div>

<!-- brand -->
<span class="abs brand-mark"></span>
<div class="abs brand-name">VITALBLOOM</div>
<div class="abs brand-sub">ENTERPRISES</div>

<!-- cart -->
<div class="abs cart">
  <svg class="abs" style="left:0;top:2px" width="26" height="22" viewBox="0 0 26 22"><path d="M1 2h4l3 12h13l3-9H7" fill="none" stroke="#bbb" stroke-width="2"/><circle cx="10" cy="18" r="2" fill="#bbb"/><circle cx="19" cy="18" r="2" fill="#bbb"/></svg>
  <div class="abs cart-title">Shopping Cart</div>
  <div class="abs cart-note">Your cart is currently empty</div>
  <a class="abs cart-link" href="#">VIEW CART ▸</a>
</div>

<!-- navigation -->
<nav>
  <a class="abs nav-tab" style="left:30px;width:82px">HOME</a>
  <a class="abs nav-tab" style="left:114px;width:84px">DETOX</a>
  <a class="abs nav-tab" style="left:199px;width:124px">HYDRATION</a>
  <a class="abs nav-tab" style="left:324px;width:144px">SUPPLEMENTS</a>
  <a class="abs nav-tab" style="left:469px;width:197px">YOUR HEALTH ISSUES</a>
</nav>
<div class="abs search-tab">
  <div class="abs search-input">Search</div>
  <span class="abs search-btn"></span>
</div>

<!-- assurance bar -->
<div class="abs assure">
  <svg class="abs" style="left:14px;top:8px" width="38" height="50" viewBox="0 0 38 50"><path d="M9 22V14a10 10 0 0 1 20 0v8" fill="none" stroke="#777" stroke-width="5"/><rect x="2" y="21" width="34" height="28" rx="3" fill="#e0a81a"/><circle cx="19" cy="33" r="4" fill="#7a5a08"/><rect x="17.5" y="34" width="3" height="8" fill="#7a5a08"/></svg>
  <div class="abs secure"><b>100% SECURE</b> FOUNDED 1996</div>
  <span class="abs pay-card" style="left:65px;background:#f4f4f4"></span>
  <span class="abs pay-card" style="left:101px;background:#f3c4a0"></span>
  <span class="abs pay-card" style="left:143px;background:#7fa9d6"></span>
  <span class="abs pay-card" style="left:182px;background:#dfe6ef" aria-label="Fundwire"></span>
  <span class="abs pay-card" style="left:220px;background:#cfd8f0"></span>
  <span class="abs divider" style="left:305px"></span>
  <div class="abs helpline">Practitioner Helpline &nbsp;/ Orders Phone Number</div>
  <div class="abs phone">01632 960 482</div>
  <span class="abs divider" style="left:617px"></span>
  <span class="abs" style="left:638px;top:12px;width:46px;height:46px;border-radius:50%;background:radial-gradient(#222 45%,var(--gold) 47%)"></span>
  <div class="abs promise" style="left:692px;top:20px"><span class="big">MONEY BACK</span><span class="small">100% GUARANTEE</span></div>
  <svg class="abs" style="left:805px;top:24px" width="44" height="26" viewBox="0 0 44 26"><rect x="0" y="2" width="28" height="17" fill="#3d8fd4"/><path d="M28 7h9l6 7v5H28z" fill="#2c6fae"/><circle cx="8" cy="21" r="4" fill="#333"/><circle cx="35" cy="21" r="4" fill="#333"/></svg>
  <div class="abs promise" style="left:856px;top:16px"><span class="big">SAME DAY</span><span class="big">DISPATCH</span></div>
</div>

<!-- side menu -->
<nav class="abs side-menu">
  <div class="menu-item is-top">A to Z<span class="toggle"><svg width="14" height="14" viewBox="0 0 14 14"><path d="M4 1l6 6-6 6" fill="none" stroke="#fff" stroke-width="1.5"/></svg></span></div>
  <div class="menu-item">Supplement Type<span class="toggle"><svg width="14" height="14" viewBox="0 0 14 14"><path d="M1 4l6 6 6-6" fill="none" stroke="#fff" stroke-width="1.5"/></svg></span></div>
  <div class="menu-item">Your Health Issue<span class="toggle"><svg width="14" height="14" viewBox="0 0 14 14"><path d="M1 4l6 6 6-6" fill="none" stroke="#fff" stroke-width="1.5"/></svg></span></div>
  <div class="menu-item">Expert Product Lines<span class="toggle"><svg width="14" height="14" viewBox="0 0 14 14"><path d="M1 4l6 6 6-6" fill="none" stroke="#fff" stroke-width="1.5"/></svg></span></div>
  <div class="menu-item">Detox &amp; Cleansing<span class="toggle"><svg width="14" height="14" viewBox="0 0 14 14"><path d="M1 4l6 6 6-6" fill="none" stroke="#fff" stroke-width="1.5"/></svg></span></div>
  <div class="menu-item">Hydration &amp; Water<span class="toggle"><svg width="14" height="14" viewBox="0 0 14 14"><path d="M1 4l6 6 6-6" fill="none" stroke="#fff" stroke-width="1.5"/></svg></span></div>
  <div class="menu-item">Natural Body Care<span class="toggle"><svg width="14" height="14" viewBox="0 0 14 14"><path d="M1 4l6 6 6-6" fill="none" stroke="#fff" stroke-width="1.5"/></svg></span></div>
  <div class="menu-item">Sport &amp; Fitness<span class="toggle"><svg width="14" height="14" viewBox="0 0 14 14"><path d="M4 1l6 6-6 6" fill="none" stroke="#fff" stroke-width="1.5"/></svg></span></div>
  <div class="menu-item">Health Technology<span class="toggle"><svg width="14" height="14" viewBox="0 0 14 14"><path d="M4 1l6 6-6 6" fill="none" stroke="#fff" stroke-width="1.5"/></svg></span></div>
  <div class="menu-item">Household Products<span class="toggle"><svg width="14" height="14" viewBox="0 0 14 14"><path d="M4 1l6 6-6 6" fill="none" stroke="#fff" stroke-width="1.5"/></svg></span></div>
  <div class="menu-item">Laboratory Tests<span class="toggle"><svg width="14" height="14" viewBox="0 0 14 14"><path d="M4 1l6 6-6 6" fill="none" stroke="#fff" stroke-width="1.5"/></svg></span></div>
  <div class="menu-item">Books &amp; Education<span class="toggle"><svg width="14" height="14" viewBox="0 0 14 14"><path d="M4 1l6 6-6 6" fill="none" stroke="#fff" stroke-width="1.5"/></svg></span></div>
  <div class="menu-item">New &amp; Special Offers<span class="toggle"><svg width="14" height="14" viewBox="0 0 14 14"><path d="M4 1l6 6-6 6" fill="none" stroke="#fff" stroke-width="1.5"/></svg></span></div>
</nav>

<div class="abs newsletter">
  <div class="nl-title"><span>SIGN UP FOR OUR</span><strong>NEWSLETTER</strong></div>
  <div class="abs nl-input">Your email address</div>
  <div class="abs nl-btn">SIGN UP</div>
</div>

<!-- category grid -->
<section>
  <div class="abs cat" style="left:221px;top:235px">
    <div class="pic" role="img" aria-label="Photo of hands forming a heart over a bare stomach" style="background:linear-gradient(90deg,#fff,#f2dccd 40%,#e9c8b4)"></div>
    <h3>DIGESTION</h3>
    <ul><li>Constipation</li><li>Candida</li><li>Irritable Bowel</li><li>Wind</li></ul>
  </div>
  <div class="abs cat" style="left:509px;top:235px">
    <div class="pic" role="img" aria-label="Illustration of a back with the painful area highlighted red" style="width:175px;background:linear-gradient(90deg,#fff,#ddd 40%,#c9c9c9 70%,#e7a49c)"></div>
    <h3>PAIN</h3>
    <ul><li>Back Pain</li><li>Joint and Bone</li><li>Headaches</li><li>Period Pain</li></ul>
  </div>
  <div class="abs cat" style="left:221px;top:377px">
    <div class="pic" role="img" aria-label="Photo of a slim waist with a tape measure" style="background:linear-gradient(90deg,#fff,#e8b08a 40%,#c98561)"></div>
    <h3>WEIGHT LOSS</h3>
    <ul><li>Without Dieting</li><li>Supplements</li><li>Sugar Metabolism</li></ul>
  </div>
  <div class="abs cat" style="left:509px;top:377px">
    <div class="pic" role="img" aria-label="Illustration of pink and blue gender symbols" style="left:82px;width:72px;background:linear-gradient(120deg,#fff,#e9a9c6 45%,#9ec7e6)"></div>
    <h3>FEMALE HEALTH</h3>
    <h3 style="left:171px">MALE HEALTH</h3>
    <ul><li>Constipation</li><li>Candida</li><li>Irritable Bowel</li><li>Wind</li></ul>
    <ul style="left:171px"><li>Back Pain</li><li>Joint and Bone</li><li>Headaches</li><li>Period Pain</li></ul>
  </div>
  <div class="abs cat" style="left:221px;top:518px">
    <div class="pic" role="img" aria-label="Illustration of a human heart" style="background:radial-gradient(ellipse 35px 50px at 50% 50%,#a3222b,#c84a4e 60%,#fff 100%)"></div>
    <h3>CARDIOVASCULAR</h3>
    <ul><li>Blood Pressure</li><li>Cholesterol</li><li>Heart &amp; Arteries</li></ul>
  </div>
  <div class="abs cat" style="left:509px;top:518px">
    <div class="pic" role="img" aria-label="Illustration of a stethoscope forming a cross" style="background:linear-gradient(90deg,#fff,#f2dede 50%,#eed3d3)"></div>
    <h3>HEALTH DEVICES</h3>
    <ul><li>Zapping</li><li>Cardiovascular</li><li>Ozone</li><li>Allergy Test</li></ul>
  </div>
  <div class="abs cat" style="left:221px;top:659px">
    <div class="pic" role="img" aria-label="Illustration of a brain with a stethoscope" style="background:radial-gradient(ellipse 55px 40px at 55% 42%,#c7826f,#e2b8ab 60%,#fff 100%)"></div>
    <h3>BRAIN HEALTH</h3>
    <ul><li>Memory</li><li>Headaches</li><li>Cognitive Function</li><li>Mood &amp; Sleep</li></ul>
  </div>
  <div class="abs cat" style="left:509px;top:659px">
    <div class="pic" role="img" aria-label="Photo of a water splash" style="background:radial-gradient(ellipse 60px 40px at 55% 60%,#a9d6ef,#def0fa 60%,#fff 100%)"></div>
    <h3>WATER &amp; HYDRATION</h3>
    <ul><li>Water Filtration</li><li>Electrolytes</li><li>Super-Hydration</li></ul>
  </div>
  <div class="abs cat" style="left:221px;top:801px">
    <div class="pic" role="img" aria-label="Photo of a woman's legs, body care" style="width:170px;background:linear-gradient(90deg,#fff,#f3e4da 40%,#e5c6b3)"></div>
    <h3>BODY CARE</h3>
    <ul><li>Anti Aging</li><li>Cosmetics</li><li>Skin Range</li><li>Face &amp; Mouth</li><li>Hair Care</li></ul>
  </div>
  <div class="abs cat" style="left:509px;top:801px">
    <div class="pic" role="img" aria-label="Photo of fresh green wheatgrass" style="background:linear-gradient(90deg,#fff,#b9dc6c 45%,#6fae2a)"></div>
    <h3>DETOX</h3>
    <ul><li>Heavy Metal Detox</li><li>Parasite Cleanse</li><li>Kidney Cleanse</li><li>Liver Cleanse</li><li>Colon Cleanse</li></ul>
  </div>
</section>

<!-- right column -->
<aside>
  <div class="abs promo hub">
    <div class="hub-head">Clinician Nook</div>
    <div class="abs" role="img" aria-label="Photo of a smiling natural health practitioner" style="left:82px;top:33px;width:100px;height:121px;background:linear-gradient(90deg,#ffeccf,#c98d67 55%,#7a4a2f)"></div>
    <div class="abs promo-copy" style="left:9px;top:48px;font-size:15px">Contact a<br>Natural<br>Health<br>Practitioner</div>
  </div>
  <div class="abs promo dental">
    <div class="hub-head" style="font-size:17px;padding:4px 3px">Amalgam Clear Dental</div>
    <div class="abs" role="img" aria-label="Photo of a smile during a dental check-up" style="left:70px;top:33px;width:112px;height:121px;background:linear-gradient(90deg,#fff,#f3cfc4 40%,#e7a79a)"></div>
    <div class="abs promo-copy" style="left:7px;top:42px;font-size:16px">A<br>comprehensive<br>list<br><span style="color:#2a9fc9">available<br>here.</span></div>
  </div>
  <div class="abs promo basket">
    <div class="abs basket-tag">Shopping<br>Basket</div>
    <div class="abs" style="left:9px;top:60px;font-size:11.5px;font-weight:600;line-height:1.3;color:#222;white-space:nowrap">You have no<br>items in your<br>shopping basket.</div>
    <svg class="abs" style="left:110px;top:50px" width="58" height="56" viewBox="0 0 58 56"><path d="M14 20l10-16M44 20L34 4" stroke="#555" stroke-width="3" fill="none"/><rect x="2" y="20" width="54" height="8" rx="2" fill="#c9171f"/><path d="M6 28h46l-5 26H11z" fill="#e02228"/></svg>
  </div>
  <div class="abs promo stores">
    <div class="abs" role="img" aria-label="Illustration of a laptop showing an online shop" style="left:28px;top:8px;width:126px;height:104px;background:linear-gradient(#f6f6f6,#d9d9d9);border-radius:6px 6px 2px 2px"></div>
    <div class="abs stores-copy">Storefronts for<br>Therapists</div>
  </div>
</aside>

<!-- footer -->
<footer>
  <div class="abs footer">
    <ul class="abs foot-col" style="left:15px"><li>Kidney Pain</li><li>Kidney Stones</li><li>Kidney Disease Symptoms</li><li>Colon Cleanse</li></ul>
    <ul class="abs foot-col" style="left:213px"><li>Digestive Enzymes</li><li>Digestive Enzymes Supplement</li><li>Healing Principles</li><li>Herbal Remedies</li></ul>
    <ul class="abs foot-col" style="left:445px"><li>Herbal Remedies for Anxiety</li><li>Herbal Remedies for Constipation</li><li>Herbal Remedies for Depression</li><li>Herbal Remedies for Menopause</li></ul>
    <ul class="abs foot-col" style="left:722px"><li>Bloated Stomach</li><li>Health Shops</li><li>Digestra</li><li>What is Amalgam Clear Dental?</li></ul>
    <div class="abs foot-links"><a>About Us</a><a>Search Terms</a><a>Advanced Search</a><a>Terms &amp; Conditions</a><a>Privacy Policy</a><a>Contact Us</a></div>
  </div>
  <span class="abs base-line"></span>
  <span class="abs base-mark"></span>
  <div class="abs copyright">© 2010 VitalBloom Enterprises. All Rights Reserved.</div>
</footer>

</body>
</html>
```